Corvatel Website Graphic design

we want a replacement of existing designs in our existing website.. we want you to suggest and create a better graphical designs which suits our service with good representation explaining our process and services
Website Url: https://corvatelq.example
Basic Requirements -
1. Flat architecture
2. A good color palette
3. Icons to support the Content
4. Consistent Images in alignment with the Business
5. Use white space to let the Content breathe

Target Market(s)

Manufacturers & E-Commerce Distributors

Industry/Entity Type

Data Service

Colors

Designer to choose colors to be used in the design.

Requirements
Must have
• Creativity and originality
Nice to have
• Try to keep it Simple

```html
<!DOCTYPE html>
<html lang="en">
<head>
<meta charset="utf-8">
<title>Corvatel Solutions</title>
<link href="https://fonts.googleapis.com/css2?family=Montserrat:wght@700;800&family=Raleway:wght@300;400;500;600;700&display=swap" rel="stylesheet">
<style>
:root{
  --ink:#1f1f24;
  --text:#3a3a44;
  --blue:#3d8ef0;
  --purple:#5b3fae;
  --violet:#7d4fa6;
  --orange:#ee9150;
  --peach:#c98a64;
  --hero-bg:#ececec;
  --footer:#141414;
  --white:#ffffff;
}
*{margin:0;padding:0;box-sizing:border-box}
html,body{width:1200px;height:4329px;overflow:hidden}
body{font-family:'Raleway',sans-serif;color:var(--text);background:var(--white);position:relative}
.btn{position:absolute;display:flex;align-items:center;justify-content:center;gap:12px;background:var(--blue);color:var(--white);border-radius:26px;font-weight:500;letter-spacing:.3px;box-shadow:0 6px 14px rgba(61,142,240,.3);text-decoration:none}
.btn svg{width:18px;height:18px}
.brand-mark{display:inline-block;width:34px;height:34px;border-radius:50%;background:var(--blue)}
.section-icon{position:absolute;width:44px;height:44px;border-radius:50%;border:5px solid var(--violet)}

/* hero */
.hero{position:absolute;left:0;top:0;width:1200px;height:652px;background:var(--hero-bg)}
.hero-shapes{position:absolute;left:0;top:0}
.logo{position:absolute;left:67px;top:20px;display:flex;align-items:center;gap:10px}
.logo-name{font-weight:600;font-size:26px;line-height:26px;color:var(--ink)}
.nav{position:absolute;top:40px;left:323px;font-size:13px}
.nav a{position:absolute;white-space:nowrap;text-decoration:none;color:var(--ink)}
.nav a.active{color:var(--blue)}
.social{position:absolute;top:31px;width:32px;height:32px;border-radius:50%;border:2px solid var(--white);display:flex;align-items:center;justify-content:center}
.social::after{content:"";width:10px;height:10px;border-radius:50%;background:var(--white)}
.hero-title{position:absolute;left:65px;top:198px;font-family:'Montserrat',sans-serif;font-weight:800;font-size:72px;line-height:76px;color:var(--ink);letter-spacing:1px}
.hero-sub{position:absolute;left:67px;top:376px;width:390px;font-size:17px;line-height:25px;color:var(--ink)}
.dots{position:absolute;left:69px;top:572px;display:flex;gap:10px}
.dots span{width:12px;height:12px;border-radius:50%;border:1.5px solid var(--ink)}
.dots span.on{background:var(--blue);border-color:var(--blue)}
.laptop-screen{position:absolute;left:677px;top:114px;width:540px;height:430px;background:var(--white);border-radius:16px 0 0 0;box-shadow:0 10px 30px rgba(0,0,0,.12)}
.laptop-art{position:absolute;left:32px;top:31px;width:500px;height:376px;background:
  radial-gradient(circle at 62% 58%,rgba(238,145,80,.55) 0 12%,transparent 26%),
  radial-gradient(circle at 40% 62%,rgba(58,160,170,.6) 0 10%,transparent 24%),
  linear-gradient(150deg,#eeedfc 0%,#c9c5f4 40%,#6a57c6 75%,#3a2a8a 100%)}
.laptop-base{position:absolute;left:660px;top:544px;width:540px;height:14px;background:linear-gradient(#f4f4f6,#cfd0d6);border-radius:8px 0 0 8px;box-shadow:0 6px 12px rgba(0,0,0,.15)}
.laptop-base::before{content:"";position:absolute;left:250px;top:0;width:90px;height:5px;background:#dcdde2;border-radius:0 0 6px 6px}

/* about */
.about-photo{position:absolute;left:143px;top:874px;width:437px;height:322px;border:3px solid var(--blue);border-radius:150px;padding:8px;background:var(--white)}
.about-photo div{width:100%;height:100%;border-radius:140px;background:
  radial-gradient(ellipse at 30% 70%,#05080d 0 22%,transparent 40%),
  radial-gradient(ellipse at 72% 70%,#05080d 0 22%,transparent 40%),
  linear-gradient(180deg,#2d6f9c 0%,#1a3f60 45%,#0a121c 100%)}
.about-title{position:absolute;left:600px;top:862px;font-size:29px;color:var(--ink);font-weight:400}
.about-title b{font-weight:700}
.about-text{position:absolute;left:600px;top:932px;width:444px;font-size:11.6px;line-height:20.2px;text-align:justify;color:var(--text)}

/* services */
.services{position:absolute;left:0;top:1277px;width:1200px;height:776px;background:linear-gradient(110deg,var(--purple) 0%,var(--violet) 45%,var(--peach) 100%)}
.services .section-icon{border-color:var(--white)}
.services-title{position:absolute;left:0;width:1200px;top:120px;text-align:center;font-size:29px;font-weight:400;color:var(--white)}
.card{position:absolute;width:444px;height:234px;background:var(--white);border:2px solid #f1eef7}
.card.featured{background:linear-gradient(135deg,#3d86ee,#5cb0f8);color:var(--white);border:none}
.card-art{position:absolute;left:22px;top:62px;width:170px;height:110px;border-radius:50%;background:radial-gradient(circle at 45% 50%,#f3b25c 0 12%,#6f8ef0 13% 32%,#dfe6fb 33% 60%,transparent 61%)}
.featured .card-art{background:radial-gradient(circle at 50% 50%,#f3b25c 0 10%,#ffffff 11% 40%,rgba(255,255,255,.35) 41% 62%,transparent 63%)}
.card h3{position:absolute;left:210px;font-weight:500;font-size:24px;line-height:26px;color:var(--ink)}
.featured h3{color:var(--white)}
.card p{position:absolute;left:210px;width:220px;font-size:9px;line-height:13px;color:var(--text)}
.featured p{color:var(--white)}
.card .mini{position:absolute;left:210px;width:64px;height:20px;border-radius:10px;background:var(--blue);color:var(--white);font-size:7px;font-weight:600;display:flex;align-items:center;justify-content:center}
.featured .mini{background:var(--white);color:var(--blue)}

/* value */
.center-title{position:absolute;left:0;width:1200px;text-align:center;color:var(--ink)}
.rule{position:absolute;width:62px;height:3px;background:var(--blue);left:569px}
.bubble{position:absolute;width:246px;height:246px;border-radius:50%;border:2px dashed #9fc2f5;background:var(--white);display:flex;align-items:center;justify-content:center}
.bubble div{width:170px;height:120px;border-radius:50%;background:radial-gradient(circle at 50% 50%,#f3b25c 0 12%,#6f8ef0 13% 30%,#dfe6fb 31% 62%,transparent 63%)}
.bubble.solid{border:none;background:linear-gradient(135deg,#3d86ee,#5cb0f8)}
.bubble.solid div{background:radial-gradient(circle at 50% 50%,#f3b25c 0 10%,#ffffff 11% 40%,rgba(255,255,255,.35) 41% 62%,transparent 63%)}
.bubble-label{position:absolute;width:300px;text-align:center;font-size:17px;line-height:20px;font-weight:500;color:var(--ink)}
.bubble-label.hi{color:var(--blue)}

/* blog */
.post-img{position:absolute;width:430px;height:240px}
.post-badges{position:absolute;left:0;top:0;width:52px}
.post-badges div{height:52px;background:var(--blue);color:var(--white);display:flex;flex-direction:column;align-items:center;justify-content:center;border-bottom:1px solid rgba(255,255,255,.35)}
.post-badges .day{font-size:17px;font-weight:600;line-height:17px}
.post-badges .mon{font-size:9px}
.post-title{position:absolute;font-size:22px;font-weight:500;line-height:28px;letter-spacing:.3px;color:var(--ink);display:flex;gap:20px}
.post-title.hi{color:var(--blue)}

/* contact */
.map{position:absolute;left:0;top:3491px;width:593px;height:424px;background:linear-gradient(135deg,#f3f2ef,#e6e5e1)}
.map-pin{position:absolute;left:232px;top:3695px}
.contact{position:absolute;left:702px;top:3491px;width:374px;height:424px;background:linear-gradient(160deg,#4b93f1,#6bb3f8);color:var(--white)}
.contact h2{position:absolute;left:0;width:100%;top:38px;text-align:center;font-size:29px;font-weight:600;letter-spacing:1px}
.contact p{position:absolute;left:30px;width:314px;top:88px;text-align:center;font-size:11.5px;line-height:16px}
.field{position:absolute;left:30px;width:314px;border-bottom:1px solid rgba(255,255,255,.7);font-size:11px;padding-bottom:18px}
.contact .send{position:absolute;left:106px;top:352px;width:164px;height:40px;border-radius:20px;background:var(--white);color:var(--blue);font-size:13px;font-weight:600;display:flex;align-items:center;justify-content:center}

/* footer */
.footer{position:absolute;left:0;top:3978px;width:1200px;height:351px;background:var(--footer);color:var(--white)}
.footer-logo{position:absolute;left:0;width:1200px;top:52px;display:flex;justify-content:center;align-items:center;gap:10px}
.footer-logo span{font-size:28px;font-weight:600}
.footer-text{position:absolute;left:155px;width:890px;top:138px;text-align:center;font-size:11.6px;line-height:21px;font-weight:500}
.footer-nav{position:absolute;left:0;width:1200px;top:222px;display:flex;justify-content:center;gap:26px;font-size:16px;align-items:center}
.footer-nav i{width:6px;height:6px;background:var(--white);border-radius:50%;display:inline-block}
.copyright{position:absolute;left:0;width:1200px;top:288px;text-align:center;font-size:11.5px}
</style>
</head>
<body>

<section class="hero">
  <svg class="hero-shapes" width="1200" height="745" viewBox="0 0 1200 745">
    <defs>
      <linearGradient id="heroPurple" x1="0" y1="0" x2="1" y2="1">
        <stop offset="0" stop-color="#6a3fa8"/>
        <stop offset="1" stop-color="#9a5f9c"/>
      </linearGradient>
    </defs>
    <path d="M740 0 H1200 V560 H640 C580 440 610 240 740 0 Z" fill="url(#heroPurple)"/>
    <circle cx="900" cy="420" r="325" fill="var(--orange)"/>
  </svg>
  <div class="laptop-screen"><div class="laptop-art" role="img" aria-label="Isometric illustration of a data dashboard platform with charts"></div></div>
  <div class="laptop-base"></div>

  <div class="logo"><span class="brand-mark"></span><span class="logo-name">Corvatel<br>Solutions</span></div>
  <nav class="nav">
    <a class="active" style="left:0;top:0">Home</a>
    <a style="left:57px;top:0">About</a>
    <a style="left:117px;top:0">Services</a>
    <a style="left:205px;top:0">Solutions</a>
    <a style="left:284px;top:0">Contact</a>
  </nav>
  <span class="social" style="left:1049px"></span>
  <span class="social" style="left:1101px"></span>

  <h1 class="hero-title">CORVATEL<br>SOLUTIONS</h1>
  <p class="hero-sub">Get your business critical data seamlessly integrated into your systems.</p>
  <a class="btn" style="left:67px;top:454px;width:202px;height:57px;font-size:17px">ABOUT US
    <svg viewBox="0 0 18 18"><path d="M2 9h13M10 4l5 5-5 5" fill="none" stroke="#fff" stroke-width="2"/></svg></a>
  <div class="dots"><span class="on"></span><span></span><span></span><span></span></div>
</section>

<div class="about-photo"><div role="img" aria-label="Photo of two engineers in front of monitoring screens in a data center"></div></div>
<span class="section-icon" style="left:600px;top:812px"></span>
<h2 class="about-title">ABOUT <b>CORVATEL SOLUTIONS</b></h2>
<p class="about-text">We provide complete spectrum of data services including data discovery, data cleansing, data enrichment, de-duplication and management to manufacturers, retailers, wholesalers, distributors, suppliers, and e-Commerce businesses. Our services are product agnostic: covering a wide array of EAM/PLM/PIM/MDM COTS platforms. The scope of our service includes, information management and data quality improvement considering various data sources like BOMs, drawings, spec sheets, legacy data and more. What sets us apart is our ability to apply domain and functional specialization in delivering data services for Engineering, Manufacturing, Distribution, Retail, Oil &amp; Gas Exploration, Defence, Food &amp; Beverage and Health Sciences domains.</p>
<a class="btn" style="left:600px;top:1156px;width:163px;height:40px;font-size:13px">READ MORE
  <svg viewBox="0 0 18 18"><path d="M2 9h13M10 4l5 5-5 5" fill="none" stroke="#fff" stroke-width="2"/></svg></a>

<section class="services">
  <span class="section-icon" style="left:578px;top:70px"></span>
  <h2 class="services-title"><b>OUR</b> SERVICES</h2>

  <article class="card" style="left:143px;top:207px">
    <div class="card-art" role="img" aria-label="Illustration of people working on data quality"></div>
    <h3 style="top:62px">Data Services</h3>
    <p style="top:102px">Data Quality determines the effectiveness of an ERP / PLM / MDM / e-Commerce system.</p>
    <span class="mini" style="top:148px">READ MORE</span>
  </article>
  <article class="card featured" style="left:600px;top:207px">
    <div class="card-art" role="img" aria-label="Illustration of a team analysing charts"></div>
    <h3 style="left:200px;top:42px">PLM/EAM/MDM<br>Data Management<br>services</h3>
    <p style="left:200px;top:132px">Data Quality determines the effectiveness of an ERP / PLM / MDM / e-Commerce system.</p>
    <span class="mini" style="left:200px;top:175px">READ MORE</span>
  </article>
  <article class="card" style="left:143px;top:457px">
    <div class="card-art" role="img" aria-label="Illustration of product data tiles being configured"></div>
    <h3 style="left:195px;top:22px">Product Data<br>configuration for<br>PIM on e-commerce<br>platform</h3>
    <p style="left:195px;top:140px">Data Quality determines the effectiveness of an ERP / PLM / MDM / e-Commerce system.</p>
    <span class="mini" style="left:195px;top:183px">READ MORE</span>
  </article>
  <article class="card" style="left:600px;top:457px">
    <div class="card-art" role="img" aria-label="Illustration of gears and people representing industries"></div>
    <h3 style="left:197px;top:44px">Services In All<br>Industry Verticals</h3>
    <p style="left:197px;top:112px">Corvatel verticals fan out into various industries. We are a company with significant subject matter expertise and experience.</p>
    <span class="mini" style="left:197px;top:168px">READ MORE</span>
  </article>
</section>

<span class="section-icon" style="left:574px;top:2134px"></span>
<h2 class="center-title" style="top:2194px;font-size:29px;font-weight:400">BETTER DATA <b>BETTER DECISIONS</b> BETTER ROI</h2>
<p class="center-title" style="top:2232px;font-size:29px;font-weight:300;line-height:33px">Our value added services help companies realize the full potential<br>of ERP and e-Commerce implementations.</p>
<span class="rule" style="top:2325px"></span>

<div class="bubble" style="left:158px;top:2367px"><div role="img" aria-label="Illustration of master data management"></div></div>
<div class="bubble solid" style="left:470px;top:2367px"><div role="img" aria-label="Illustration of e-commerce data configuration"></div></div>
<div class="bubble" style="left:778px;top:2367px"><div role="img" aria-label="Illustration of support services"></div></div>
<p class="bubble-label" style="left:131px;top:2650px">MASTER DATA<br>MANAGEMENT</p>
<p class="bubble-label hi" style="left:443px;top:2650px">E-COMMERCE DATA<br>CONFIGURATION</p>
<p class="bubble-label" style="left:756px;top:2650px">SUPPORT<br>SERVICES</p>

<span class="section-icon" style="left:574px;top:2776px"></span>
<h2 class="center-title" style="top:2832px;font-size:29px;font-weight:400"><b>OUR</b> BLOG</h2>
<p class="center-title" style="top:2872px;font-size:29px;font-weight:300;line-height:33px">Operating with a bad data is more expensive than the cost of<br>improving data quality</p>
<span class="rule" style="top:2964px"></span>

<div class="post-img" style="left:146px;top:2999px;background:radial-gradient(ellipse at 25% 35%,#7a2a30 0 10%,transparent 30%),linear-gradient(135deg,#4a4a4c,#18181a)" role="img" aria-label="Photo of a hand holding a payment card near a laptop">
  <div class="post-badges">
    <div><span class="day">01</span><span class="mon">DEC</span></div>
    <div><svg width="22" height="20" viewBox="0 0 24 22"><path d="M12 21 2.5 11.5A5.5 5.5 0 0 1 12 4a5.5 5.5 0 0 1 9.5 7.5Z" fill="#fff"/></svg></div>
    <div><svg width="24" height="20" viewBox="0 0 24 20"><ellipse cx="11" cy="9" rx="10" ry="7" fill="#fff"/><path d="M4 13 2 19 9 15Z" fill="#fff"/></svg></div>
  </div>
</div>
<div class="post-img" style="left:613px;top:2999px;background:radial-gradient(ellipse at 60% 45%,#2f4560 0 20%,transparent 55%),linear-gradient(135deg,#1c2838,#0c121b)" role="img" aria-label="Photo of code on a dark screen">
  <div class="post-badges">
    <div><span class="day">01</span><span class="mon">DEC</span></div>
    <div><svg width="22" height="20" viewBox="0 0 24 22"><path d="M12 21 2.5 11.5A5.5 5.5 0 0 1 12 4a5.5 5.5 0 0 1 9.5 7.5Z" fill="#fff"/></svg></div>
    <div><svg width="24" height="20" viewBox="0 0 24 20"><ellipse cx="11" cy="9" rx="10" ry="7" fill="#fff"/><path d="M4 13 2 19 9 15Z" fill="#fff"/></svg></div>
  </div>
</div>
<p class="post-title" style="left:146px;top:3266px">10 Best Practices in E-commerce
  <svg width="28" height="28" viewBox="0 0 28 28"><path d="M2 14h22M16 6l8 8-8 8" fill="none" stroke="#1f1f24" stroke-width="2"/></svg></p>
<p class="post-title hi" style="left:613px;top:3266px;width:430px">Best Practices – Successful Data<br>Cleaning
  <svg style="position:absolute;left:380px;top:0" width="28" height="28" viewBox="0 0 28 28"><path d="M2 14h22M16 6l8 8-8 8" fill="none" stroke="#3d8ef0" stroke-width="2"/></svg></p>
<a class="btn" style="left:504px;top:3363px;width:163px;height:42px;font-size:14px">VIEW MORE
  <svg viewBox="0 0 18 18"><path d="M2 9h13M10 4l5 5-5 5" fill="none" stroke="#fff" stroke-width="2"/></svg></a>

<div class="map" role="img" aria-label="Street map showing the office location"></div>
<svg class="map-pin" width="22" height="30" viewBox="0 0 22 30"><path d="M11 29C11 29 2 17 2 11a9 9 0 0 1 18 0c0 6-9 18-9 18Z" fill="#e2403a"/><circle cx="11" cy="11" r="3.5" fill="#fff"/></svg>
<section class="contact">
  <h2>GET IN TOUCH</h2>
  <p>We'd love to hear from you. If you've got questions, feedback or ideas you would like to share. For anything more specific, please use form below.</p>
  <div class="field" style="top:165px">FULL NAME</div>
  <div class="field" style="top:230px">EMAIL</div>
  <div class="field" style="top:300px">MESSAGE</div>
  <span class="send">SEND MESSAGE</span>
</section>

<footer class="footer">
  <div class="footer-logo"><span class="brand-mark"></span><span>Corvatel Solutions</span></div>
  <p class="footer-text">Corvatel Solutions specializes in extracting business centric information from large, complex and disparate sources to realize full potential of Enterprise and e-Commerce implementations.</p>
  <nav class="footer-nav"><span>HOME</span><i></i><span>ABOUT</span><i></i><span>SERVICES</span><i></i><span>SOLUTIONS</span><i></i><span>Contact Us</span></nav>
  <p class="copyright">Copyright © CORVATEL SOLUTIONS 2019. All rights reserved.</p>
</footer>

</body>
</html>
```